Freelance business trainer needs a new business card

My business is called Tbrite. I provide training in the workplace on management, coaching and mentoring, and customer service topics for a variety of businesses, colleges and private training providers, and teach on management programs. I need a professional but eye catching business card. Business colours grey and orange. My name Linda Marchbank; Tel 07853 416207; email lmarchbank@tbrite.co.uk; website www.tbrite.co.uk.
Happy to have some sort of logo on front and details on back or all on one side
Target Market(s)
SME businesses and colleges - workshops i run are for adults in the workplace
Industry/Entity Type
Training
Look and feel

```html
<!DOCTYPE html>
<html lang="en">
<head>
<meta charset="utf-8">
<title>Tbrite – Business Card</title>
<link href="https://fonts.googleapis.com/css2?family=Barlow:wght@400;500;600;700&display=swap" rel="stylesheet">
<style>
  :root {
    --orange: #f7941d;
    --orange-soft: #f9aa4c;
    --grey: #6d6e70;
    --grey-soft: #7b7c7e;
    --white: #f4f4f4;
    --backdrop: #e4e4e4;
  }
  * { box-sizing: border-box; margin: 0; padding: 0; }
  html, body { width: 1200px; height: 800px; overflow: hidden; }
  body {
    background: var(--backdrop);
    font-family: "Barlow", Arial, sans-serif;
    position: relative;
  }
  .card {
    position: absolute;
    top: 250px;
    width: 510px;
    height: 300px;
    overflow: hidden;
    box-shadow: 0 4px 14px rgba(0,0,0,0.18);
  }
  .card-front { left: 60px; background: var(--orange); }
  .card-back { left: 630px; background: var(--grey); }
  .decor { position: absolute; inset: 0; }

  /* front */
  .front-band { position: absolute; left: 0; top: 0; width: 100%; height: 40px; background: var(--white); }
  .front-rule { position: absolute; left: 0; top: 40px; width: 100%; height: 5px; background: var(--grey); }
  .tagline {
    position: absolute; left: 120px; top: 70px;
    color: var(--white); font-size: 17px; font-weight: 400; letter-spacing: 0.2px;
  }
  .front-logo {
    position: absolute; left: 120px; top: 115px;
    display: flex; align-items: center; gap: 14px;
  }
  .front-logo .name {
    color: var(--white); font-size: 104px; font-weight: 500; line-height: 1; letter-spacing: 1px;
  }
  .front-logo .dot { width: 18px; height: 18px; border-radius: 50%; background: var(--grey); margin-top: 46px; }

  /* back */
  .back-band-top { position: absolute; left: 0; top: 0; width: 100%; height: 34px; background: var(--white); }
  .back-band-bottom { position: absolute; left: 0; bottom: 0; width: 100%; height: 22px; background: var(--white); }
  .accent-top { position: absolute; left: 0; top: 34px; width: 270px; height: 4px; background: var(--orange); }
  .accent-bottom { position: absolute; right: 0; bottom: 22px; width: 90px; height: 4px; background: var(--orange); }
  .website {
    position: absolute; right: 18px; top: 7px;
    color: var(--orange); font-size: 17px; font-weight: 500; letter-spacing: 2.5px;
  }
  .holder { position: absolute; left: 24px; top: 56px; color: var(--white); }
  .holder .person { color: var(--orange); font-size: 19px; font-weight: 700; letter-spacing: 0.5px; text-transform: uppercase; }
  .holder .role, .holder .creds { font-size: 11.5px; line-height: 1.3; }
  .contact { position: absolute; left: 24px; top: 130px; color: var(--white); font-size: 14px; line-height: 1.45; }
  .contact .label { color: var(--orange); margin-right: 4px; }
  .back-logo {
    position: absolute; right: 40px; top: 118px;
    display: flex; align-items: center; gap: 10px;
  }
  .back-logo .name { color: var(--white); font-size: 62px; font-weight: 500; line-height: 1; }
  .back-logo .dot { width: 12px; height: 12px; border-radius: 50%; background: var(--orange); margin-top: 28px; }
  .address {
    position: absolute; left: 200px; top: 190px;
    color: var(--white); font-size: 14px; line-height: 1.3; font-style: normal;
  }
</style>
</head>
<body>

<section class="card card-front" aria-label="Card front">
  <svg class="decor" viewBox="0 0 510 300" aria-hidden="true">
    <circle cx="400" cy="70" r="150" fill="var(--orange-soft)" opacity="0.6"/>
    <circle cx="250" cy="260" r="140" fill="var(--orange-soft)" opacity="0.35"/>
  </svg>
  <div class="front-band"></div>
  <div class="front-rule"></div>
  <p class="tagline">Professional Workplace Training Services</p>
  <div class="front-logo">
    <span class="name">Tbrite</span>
    <span class="dot"></span>
  </div>
</section>

<section class="card card-back" aria-label="Card back">
  <svg class="decor" viewBox="0 0 510 300" aria-hidden="true">
    <circle cx="250" cy="230" r="100" fill="var(--grey-soft)" opacity="0.7"/>
    <circle cx="470" cy="210" r="110" fill="var(--grey-soft)" opacity="0.5"/>
  </svg>
  <div class="back-band-top"></div>
  <div class="accent-top"></div>
  <p class="website">www.tbrite.co.uk</p>

  <div class="holder">
    <p class="person">Linda Marchbank</p>
    <p class="role">Owner/Lead Trainer</p>
    <p class="creds">MCMI, MIFL, CertEd, PGCCM, TIOSH</p>
  </div>

  <div class="contact">
    <p><span class="label">[T]</span>07853 416207</p>
    <p><span class="label">[E]</span>lmarchbank@tbrite.co.uk</p>
  </div>

  <div class="back-logo">
    <span class="name">Tbrite</span>
    <span class="dot"></span>
  </div>

  <address class="address">
    Linden House<br>
    Westfield Road<br>
    Ashcombe<br>
    RG31 4PT
  </address>

  <div class="accent-bottom"></div>
  <div class="back-band-bottom"></div>
</section>

</body>
</html>
```